Business Card Design Project

This design is a slimline business card 45mm x90mm, the card will be printed at 49mm x 94mm and cut to 45mm x90 mm, this needs to be considered in the design. The content required on the front and back of the business card is attached in a pdf; the design will be done using photo shop as we use CS6 in our business. The design needs to be developed using a CMYK colour pallet, the main colours used on our business are red, grey black and white. A snapshot of our business brochure and new website has been provided to give you an understanding on our businesses look and feel.
FRONT OF BUSINESS CARD
Director
Marcus Feld
Ph+61 0421780213
www.brightvanecontracting.com.au
marcusfeld@brightvanecontracting.com.au
BACK OF BUSINESS CARD
SUPPORTING CLIENTS IN
Oil & Gas I Minerals & Metals I Petrochemical I Manufacturing
Building & Construction I Telecommunication I Rail I Civil I New Industries
KNOWLEDGE I EXPERTISE I EXPERIENCE I CAPACITY

```html
<!DOCTYPE html>
<html lang="en">
<head>
<meta charset="utf-8">
<title>Brightvane Contracting – Business Card</title>
<link rel="stylesheet" href="https://fonts.googleapis.com/css2?family=Open+Sans:wght@400;600&display=swap">
<style>
  :root {
    --brand-red: #ee2b3a;
    --brand-red-light: #f25a60;
    --brand-red-deep: #e32232;
    --ink: #1e1e1e;
    --grey: #3a3a3a;
    --paper: #ffffff;
    --backdrop: #d9d9d9;
  }
  html, body {
    margin: 0;
    padding: 0;
    width: 1200px;
    height: 1104px;
    overflow: hidden;
    background: var(--backdrop);
    font-family: "Open Sans", Arial, sans-serif;
  }
  .canvas {
    position: relative;
    width: 1200px;
    height: 1104px;
  }
  .card {
    position: absolute;
    left: 80px;
    width: 1040px;
    height: 520px;
    overflow: hidden;
    box-shadow: 0 2px 6px rgba(0,0,0,0.18);
  }
  .card--sectors { top: 20px; background: var(--paper); }
  .card--contact {
    top: 564px;
    background: linear-gradient(90deg, var(--brand-red-deep) 0%, var(--brand-red-light) 42%, var(--brand-red) 72%, var(--brand-red-deep) 100%);
    color: var(--paper);
  }

  /* Sectors side */
  .brand {
    position: absolute;
    left: 160px;
    top: 62px;
    display: flex;
    align-items: center;
    gap: 26px;
  }
  .brand__mark { width: 130px; height: 130px; flex: none; }
  .brand__text { display: flex; flex-direction: column; }
  .brand__name {
    font-size: 58px;
    font-weight: 600;
    color: var(--ink);
    letter-spacing: 1px;
    line-height: 1.05;
  }
  .brand__tagline {
    font-size: 19px;
    color: var(--ink);
    margin-top: 8px;
  }
  .divider {
    position: absolute;
    left: 62px;
    top: 284px;
    width: 918px;
    height: 4px;
    background: var(--brand-red);
  }
  .sectors {
    position: absolute;
    left: 0;
    top: 312px;
    width: 100%;
    text-align: center;
  }
  .sectors__heading {
    font-size: 26px;
    color: var(--brand-red);
    margin: 0 0 6px;
    font-weight: 400;
  }
  .sectors__line {
    font-size: 29px;
    color: var(--ink);
    margin: 0;
    line-height: 37px;
    letter-spacing: 0.6px;
  }
  .values-band {
    position: absolute;
    left: 0;
    bottom: 0;
    width: 100%;
    height: 74px;
    background: var(--brand-red);
    display: flex;
    align-items: center;
    justify-content: center;
    color: var(--paper);
    font-size: 31px;
    letter-spacing: 5px;
  }

  /* Contact side */
  .contact-name {
    position: absolute;
    top: 92px;
    width: 100%;
    text-align: center;
    font-size: 72px;
    margin: 0;
    font-weight: 400;
    line-height: 1;
  }
  .contact-role {
    position: absolute;
    top: 196px;
    width: 100%;
    text-align: center;
    font-size: 30px;
    margin: 0;
  }
  .contact-details {
    position: absolute;
    top: 346px;
    width: 100%;
    text-align: center;
    font-size: 28px;
    line-height: 37px;
  }
  .contact-details p { margin: 0; }
</style>
</head>
<body>
<main class="canvas">
  <section class="card card--sectors" aria-label="Card side with sectors">
    <div class="brand">
      <svg class="brand__mark" viewBox="0 0 130 130" aria-hidden="true">
        <circle cx="65" cy="65" r="62" fill="var(--brand-red)"/>
      </svg>
      <div class="brand__text">
        <span class="brand__name">BRIGHTVANE CONTRACTING</span>
        <span class="brand__tagline">Providing Effective Project Controls and Management Solutions</span>
      </div>
    </div>
    <div class="divider"></div>
    <div class="sectors">
      <h2 class="sectors__heading">SUPPORTING CLIENTS IN</h2>
      <p class="sectors__line">Oil &amp; Gas I Minerals &amp; Metals I Petrochemical I Manufacturing</p>
      <p class="sectors__line">Building &amp; Construction I Telecommunication I Rail I Civil I New Industries</p>
    </div>
    <div class="values-band">KNOWLEDGE I EXPERTISE I EXPERIENCE I CAPACITY</div>
  </section>

  <section class="card card--contact" aria-label="Card side with contact details">
    <h1 class="contact-name">Marcus Feld</h1>
    <p class="contact-role">Director</p>
    <div class="contact-details">
      <p>+61 0497365128</p>
      <p>www.brightvanecontracting.com.au</p>
      <p>marcusfeld@brightvanecontracting.com.au</p>
    </div>
  </section>
</main>
</body>
</html>
```